A new updated business card. A good first impression for new customers to our business.

I need something unique. I will attached a picture of our old rubbish cards, and also our current Logo ( I think this needs an update if you have any ideas, its very basic and budget)The best way you will get to see my business is checking our Facebook page, I don't really know what else to say, but anything you want to know, ask away.www.facebook.com/tkwashworksco/

Target Market(s)

Home owners

Industry/Entity Type

Business

Contact Information for Business Card

T&K's Wash Works & Surface Guarding
Mira 0462 518 309 mira@tkwashworksco.com
Dunstan 0451 236 087 dunstan@tkwashworksco.com

FB: www.facebook.com/tkwashworksco/
Website: www.tkwashworksco.net (This is pretty rubbish- we don't really use it)

100% customer satisfaction guaranteed

All aspects of Hi-Pressure Cleaning
Sealing & Re-Sealing
Roof Cleaning
Colour sealing
Decorative coatings

Free no obligation quotes

Requirements
Must have
• NO OBLIGATION FREE quotes
• 100% Customer satisfaction guaranteed
• Can you please add both names, contact details and email address on one card.
• Dunstan 0451 236 087
• dunstan@tkwashworksco.com
• Mira 0462 518 309
• mira@tkwashworksco.com
• Please change the services:
• Hot/Cold Hi-Pressure Cleaning
• Sealing & Re-Sealing
• Roof Cleaning
• Colour Sealing
• Decorative Coatings
• Concrete Honing
• Thanks
Nice to have
• Something a bit different, something eye catching.l

```html
<!DOCTYPE html>
<html lang="en">
<head>
<meta charset="utf-8">
<title>T&amp;K's Wash Works &amp; Surface Guarding – Business Card</title>
<link href="https://fonts.googleapis.com/css2?family=Open+Sans:wght@400;600;700&display=swap" rel="stylesheet">
<style>
  :root {
    --sky: #2ba6e0;
    --brand-red: #e21b23;
    --ink: #222222;
    --steel: #4a4d52;
    --paper: #ffffff;
    --backdrop: #ecebe7;
  }
  * { box-sizing: border-box; margin: 0; padding: 0; }
  html, body {
    width: 1200px; height: 950px; overflow: hidden;
    background: var(--backdrop);
    font-family: "Open Sans", Arial, sans-serif;
  }
  .canvas { position: relative; width: 1200px; height: 950px; }
  .card {
    position: absolute; left: 250px; width: 700px; height: 400px;
    border-radius: 22px; overflow: hidden;
    box-shadow: 0 10px 28px rgba(0,0,0,.18);
  }
  /* ---------- Services side ---------- */
  .card--services {
    top: 55px; background: var(--sky); color: var(--paper);
    display: flex; flex-direction: column; align-items: center; justify-content: center;
    text-align: center;
  }
  .services__brand {
    display: flex; align-items: center; gap: 16px; margin-bottom: 30px;
  }
  .services__mark {
    width: 22px; height: 22px; border-radius: 50%; background: var(--paper); flex: none;
  }
  .services__name {
    font-weight: 700; font-size: 30px; line-height: 1.15; color: var(--paper);
    text-align: left; white-space: nowrap;
  }
  .services__list { font-size: 18px; line-height: 1.55; font-weight: 400; }
  .services__quote { margin-top: 14px; font-size: 21px; font-weight: 700; }
  .services__guarantee { margin-top: 4px; font-size: 17px; font-weight: 600; }

  /* ---------- Contact side ---------- */
  .card--contact { top: 495px; background: var(--paper); }
  .contact__brand {
    position: absolute; left: 0; top: 48px; width: 100%;
    display: flex; align-items: center; justify-content: center; gap: 14px;
  }
  .contact__mark {
    width: 20px; height: 20px; border-radius: 50%; background: var(--brand-red); flex: none;
  }
  .contact__name {
    font-weight: 700; font-size: 27px; line-height: 1.15; color: var(--brand-red);
    white-space: nowrap;
  }
  .contact__people {
    position: absolute; top: 150px; left: 0; width: 100%;
    display: flex; justify-content: center;
  }
  .person { padding: 0 16px; }
  .person--left { text-align: right; border-right: 1px solid #9a9a9a; }
  .person--right { text-align: left; }
  .person__name { color: var(--brand-red); font-weight: 600; font-size: 24px; line-height: 1.2; }
  .person__phone { color: var(--ink); font-size: 22px; line-height: 1.3; }
  .person__email { color: var(--ink); font-size: 17px; line-height: 1.4; }
  .swoosh { position: absolute; left: 0; bottom: 0; }
  .footer__social {
    position: absolute; left: 24px; bottom: 24px;
    display: flex; align-items: center; gap: 10px;
    color: var(--paper); font-size: 18px;
  }
  .footer__square { width: 22px; height: 22px; background: var(--paper); border-radius: 3px; }
  .footer__web {
    position: absolute; right: 28px; bottom: 54px;
    color: var(--paper); font-size: 18px; font-weight: 600;
  }
</style>
</head>
<body>
<main class="canvas">
  <section class="card card--services">
    <div class="services__brand">
      <span class="services__mark"></span>
      <span class="services__name">T&amp;K's Wash Works &amp;<br>Surface Guarding</span>
    </div>
    <p class="services__list">Hot/Cold Hi-Pressure Cleaning &bull; Sealing &amp; Re-Sealing<br>Roof Cleaning &bull; Colour Sealing &bull; Decorative Coatings<br>Concrete Honing</p>
    <p class="services__quote">Free no obligation quotes</p>
    <p class="services__guarantee">100% customer satisfaction guaranteed</p>
  </section>

  <section class="card card--contact">
    <div class="contact__brand">
      <span class="contact__mark"></span>
      <span class="contact__name">T&amp;K's Wash Works &amp;<br>Surface Guarding</span>
    </div>

    <div class="contact__people">
      <div class="person person--left">
        <p class="person__name">Dunstan</p>
        <p class="person__phone">0451 236 087</p>
        <p class="person__email">dunstan@tkwashworksco.com</p>
      </div>
      <div class="person person--right">
        <p class="person__name">Mira</p>
        <p class="person__phone">0462 518 309</p>
        <p class="person__email">mira@tkwashworksco.com</p>
      </div>
    </div>

    <svg class="swoosh" width="700" height="150" viewBox="0 0 700 150" aria-hidden="true">
      <path d="M0 62 C 220 70, 470 40, 700 0 L700 6 C 470 46, 220 76, 0 68 Z" fill="var(--sky)"/>
      <path d="M0 74 C 220 82, 470 54, 700 14 L700 34 C 470 74, 220 98, 0 92 Z" fill="var(--steel)"/>
      <path d="M0 98 C 220 104, 470 80, 700 40 L700 150 L0 150 Z" fill="var(--brand-red)"/>
    </svg>
    <div class="footer__social">
      <span class="footer__square"></span>
      <span>tkwashworksco</span>
    </div>
    <p class="footer__web">www.tkwashworksco.net</p>
  </section>
</main>
</body>
</html>
```